Criação de Kit com 6 Layouts de Post para Redes Sociais (Facebook, Instagram e etc) + Capa de Facebook para Outros
" Atualmente, on-line. Estamos abertos há poucos meses, fazendo atendimento para outras agencias e agora vamos abrir para atendimento do público utilizando instagram, whatsapp e face como formas de captação. "

```html
<!DOCTYPE html>
<html lang="pt-BR">
<head>
<meta charset="UTF-8">
<title>Pronto pra viajar?</title>
<link rel="stylesheet" href="https://fonts.googleapis.com/css2?family=Poppins:wght@400;500;600;700&display=swap">
<style>
  :root {
    --navy: #0b2a5b;
    --blue: #2a7de1;
    --bright-blue: #1f8cf0;
    --suitcase: #2f5fe0;
    --white: #ffffff;
    --sky-top: #e9eef3;
    --sky-mid: #f4f6f8;
    --sky-low: #dfe6ee;
  }
  * { margin: 0; padding: 0; box-sizing: border-box; }
  html, body { width: 1200px; height: 1200px; overflow: hidden; }
  body { font-family: "Poppins", sans-serif; }
  .post {
    position: relative;
    width: 1200px;
    height: 1200px;
    overflow: hidden;
    background: radial-gradient(ellipse at 25% 85%, #ffffff 0%, rgba(255,255,255,0) 45%),
                radial-gradient(ellipse at 80% 20%, #ffffff 0%, rgba(255,255,255,0) 40%),
                linear-gradient(180deg, var(--sky-top) 0%, var(--sky-mid) 55%, var(--sky-low) 100%);
  }
  .flight-path { position: absolute; inset: 0; }
  .brand {
    position: absolute;
    top: 68px;
    left: 0;
    width: 1200px;
    text-align: center;
    font-weight: 700;
    font-size: 34px;
    letter-spacing: 1px;
    color: var(--blue);
  }
  .suitcase {
    position: absolute;
    left: 139px;
    top: 192px;
    width: 257px;
    height: 660px;
    border-radius: 36px;
    background: linear-gradient(90deg, #2450c8 0%, var(--suitcase) 40%, #3d6ff0 70%, #2452cc 100%);
  }
  .photo-card {
    position: absolute;
    left: 482px;
    top: 182px;
    width: 634px;
    height: 716px;
    background: var(--white);
    padding: 30px 30px 60px;
    transform: rotate(2deg);
    box-shadow: 0 14px 36px rgba(11,42,91,0.18);
  }
  .photo-card .photo {
    width: 100%;
    height: 100%;
    background: linear-gradient(180deg, #3b8fd6 0%, #7ab8e6 30%, #5d8f7a 60%, #3f6b3e 100%);
  }
  .headline {
    position: absolute;
    left: 91px;
    top: 694px;
    display: flex;
    flex-direction: column;
    align-items: flex-start;
    gap: 6px;
  }
  .headline span {
    display: inline-block;
    font-size: 64px;
    line-height: 78px;
    padding: 0 14px;
    font-weight: 500;
  }
  .headline .line-dark { background: var(--navy); color: var(--white); }
  .headline .line-light { background: var(--white); color: var(--navy); font-weight: 400; }
  .cta {
    position: absolute;
    left: 91px;
    top: 1032px;
    display: flex;
    height: 64px;
  }
  .cta .cta-arrow {
    width: 64px;
    height: 64px;
    background: var(--navy);
    display: flex;
    align-items: center;
    justify-content: center;
  }
  .cta .cta-label {
    background: var(--navy);
    color: var(--white);
    font-size: 22px;
    line-height: 64px;
    padding: 0 26px 0 8px;
    border-left: 3px solid var(--white);
  }
  .plane { position: absolute; fill: var(--bright-blue); }
  .plane-top { left: 1010px; top: 100px; width: 110px; height: 110px; transform: rotate(78deg); }
  .plane-bottom { left: 770px; top: 1060px; width: 100px; height: 100px; transform: rotate(90deg); }
</style>
</head>
<body>
<main class="post">
  <svg class="flight-path" viewBox="0 0 1200 1200" aria-hidden="true">
    <path d="M0 290 C 200 250, 330 180, 560 175 S 900 110, 1060 150" fill="none" stroke="var(--blue)" stroke-width="5" stroke-dasharray="20 14"/>
  </svg>

  <div class="brand">SEU LOGO</div>

  <svg class="plane plane-top" viewBox="0 0 24 24" aria-hidden="true">
    <path d="M21 16v-2l-8-5V3.5a1.5 1.5 0 0 0-3 0V9l-8 5v2l8-2.5V19l-2 1.5V22l3.5-1 3.5 1v-1.5L13 19v-5.5z"/>
  </svg>

  <div class="suitcase" role="img" aria-label="Mala de viagem azul com alça"></div>

  <figure class="photo-card">
    <div class="photo" role="img" aria-label="Vista aérea do Cristo Redentor sobre o Rio de Janeiro, com mar e montanhas"></div>
  </figure>

  <h1 class="headline">
    <span class="line-dark">Pronto pra viajar?</span>
    <span class="line-light">Qual o seu</span>
    <span class="line-light">próximo destino?</span>
  </h1>

  <div class="cta">
    <div class="cta-arrow">
      <svg width="26" height="26" viewBox="0 0 24 24" aria-hidden="true">
        <path d="M8 4l8 8-8 8" fill="none" stroke="#fff" stroke-width="3" stroke-linecap="round" stroke-linejoin="round"/>
      </svg>
    </div>
    <div class="cta-label">Fale conosco agora!</div>
  </div>

  <svg class="plane plane-bottom" viewBox="0 0 24 24" aria-hidden="true">
    <path d="M21 16v-2l-8-5V3.5a1.5 1.5 0 0 0-3 0V9l-8 5v2l8-2.5V19l-2 1.5V22l3.5-1 3.5 1v-1.5L13 19v-5.5z"/>
  </svg>
</main>
</body>
</html>
```